Customer flyer

Hi there,

We need a flyer done for our father's business. It is called Tidal crest and the flyer will be distributed to realtors in British Columbia. He lends money to realtors when they have sold a home from the time subjects are removed from the transaction to when the sale closes. He is looking for a modern, classy look with the following information:

"Tidal Crest"

Realtor Pay Day upon Subject Removal

Did you know?

* Fees 100% tax deductable
* Same Day Service
* Confidential
* Low Rates

Your money from 738519 B.C. Ltd. and It can be directly deposited into your bank account or delivered to your office

For quote: call Gavin Merrow 250 555 0137

This is a small business so he doesn't have a logo and has never needed to do promotions before as it's run on word of mouth for the past 10 years. We are open to all ideas and suggestions - he is a finance guy so looking to you for the creative side :)

Thank you!

I don't like the phrase Realtor Pay Day upon subject removal. I think I prefer "Realtors! Celebrate Your Home sales upon subject removal" . Your thoughts?

Thank you

```html
<!DOCTYPE html>
<html lang="en">
<head>
<meta charset="utf-8">
<title>Tidal Crest – Realtor Flyer</title>
<link rel="stylesheet" href="https://fonts.googleapis.com/css2?family=Oswald:wght@600&family=PT+Sans:ital,wght@0,400;0,700;1,400;1,700&display=swap">
<style>
  :root {
    --brand-blue: #2a6fa8;
    --brand-blue-dark: #2266a0;
    --sky: #7ccbee;
    --white: #ffffff;
    --paper-top: #fbfbfb;
    --paper-bottom: #d6d7d9;
    --photo-light: #dfe7ec;
    --photo-mid: #9fb4c2;
    --photo-dark: #3e4a55;
  }
  * { margin: 0; padding: 0; box-sizing: border-box; }
  html, body { width: 900px; height: 1200px; overflow: hidden; background: var(--white); }
  .flyer {
    position: relative;
    width: 900px;
    height: 1200px;
    overflow: hidden;
    background: linear-gradient(180deg, var(--paper-top) 45%, var(--paper-bottom) 100%);
    font-family: "PT Sans", Arial, sans-serif;
  }
  .hero-photo {
    position: absolute;
    left: 0; top: 0;
    width: 900px; height: 519px;
    background:
      radial-gradient(ellipse 260px 300px at 640px 300px, rgba(150,210,245,0.55), transparent 70%),
      linear-gradient(90deg, var(--photo-light) 0%, var(--photo-dark) 35%, var(--photo-mid) 60%, var(--photo-light) 100%);
  }
  .divider {
    position: absolute;
    left: 0; top: 515px;
    width: 900px; height: 9px;
    background: var(--brand-blue);
  }
  .brand-tab {
    position: absolute;
    left: 23px; top: 467px;
    width: 546px; height: 118px;
    background: var(--brand-blue-dark);
    border-radius: 20px;
    display: flex; align-items: center; justify-content: center;
  }
  .brand-name {
    font-family: "Oswald", "Arial Narrow", sans-serif;
    font-weight: 600;
    font-size: 70px;
    color: var(--white);
    letter-spacing: 0.5px;
  }
  .headline {
    position: absolute;
    left: 36px; top: 608px;
    width: 840px;
    color: var(--brand-blue);
    font-size: 43px;
    line-height: 53px;
  }
  .headline strong { font-weight: 700; font-size: 46px; }
  .benefits {
    position: absolute;
    left: 38px; top: 762px;
    list-style: none;
    color: var(--sky);
    font-weight: 700;
    font-size: 33px;
    line-height: 46px;
  }
  .benefits li::before { content: "• "; }
  .did-you-know {
    position: absolute;
    left: 520px; top: 700px;
    width: 360px; height: 200px;
  }
  .paragraph {
    position: absolute;
    left: 36px; top: 988px;
    width: 780px;
    color: var(--brand-blue);
    font-size: 30px;
    line-height: 38px;
  }
  .contact {
    position: absolute;
    left: 36px; top: 1118px;
    color: var(--brand-blue);
    font-size: 32px;
    white-space: nowrap;
  }
  .contact .prompt { color: var(--sky); font-style: italic; font-size: 30px; margin-right: 10px; }
  .contact .phone { font-weight: 700; font-size: 50px; margin-left: 6px; }
</style>
</head>
<body>
  <main class="flyer">
    <div class="hero-photo" role="img" aria-label="Photo of a businessman in a suit pointing at a glowing outline of a house"></div>
    <div class="divider"></div>
    <div class="brand-tab"><span class="brand-name">Tidal Crest</span></div>

    <h1 class="headline"><strong>Realtors!</strong> Celebrate Your Home sales<br>upon subject removal</h1>

    <ul class="benefits">
      <li>Fees 100% tax deductable</li>
      <li>Same Day Service</li>
      <li>Confidential</li>
      <li>Low Rates</li>
    </ul>

    <svg class="did-you-know" viewBox="0 0 360 200" aria-label="Did you know?">
      <path d="M191 4 C280 4 352 48 352 100 C352 152 280 196 191 196 C150 196 113 187 86 171 L8 188 L48 140 C36 128 30 114 30 100 C30 48 102 4 191 4 Z" fill="var(--sky)"/>
      <g transform="rotate(8 190 100)" fill="var(--white)" font-family="PT Sans, Arial, sans-serif" font-weight="700" font-style="italic" font-size="54" text-anchor="middle">
        <text x="188" y="88">Did you</text>
        <text x="188" y="140">know?</text>
      </g>
    </svg>

    <p class="paragraph">Your money from 738519 B.C. Ltd. and It can be directly deposited into your bank account or delivered to your office</p>

    <p class="contact"><span class="prompt">For quote call:</span> Gavin Merrow <span class="phone">250 555 0137</span></p>
  </main>
</body>
</html>
```